" A maioria das empresas tem dificuldades em lidar com o quadro de funcionários. A consultoria entra fornecendo todo o suporte com treinamentos para melhoria do clima e das relações interpessoais, melhoria do atendimento ao cliente, desenvolve líderes e os capacita para lidar de maneira mais adequada com os conflitos da equipe. Além disso, também realizamos todo o processo de recrutamento e seleção. Entre outros serviços. "

```html
<!DOCTYPE html>
<html lang="pt-BR">
<head>
<meta charset="UTF-8">
<title>Avante — Pasta Institucional</title>
<link rel="stylesheet" href="https://fonts.googleapis.com/css2?family=Montserrat:wght@400;500;700&display=swap">
<style>
  :root {
    --navy: #14204a;
    --navy-deep: #0e1838;
    --gold: #f2ae1c;
    --paper: #ffffff;
    --ink: #1d2547;
    --muted: #5a6078;
    --backdrop: #e9e6e1;
  }
  * { box-sizing: border-box; margin: 0; padding: 0; }
  html, body {
    width: 1200px; height: 1200px; overflow: hidden;
    background: var(--backdrop);
    font-family: "Montserrat", sans-serif;
  }
  .folder {
    position: absolute; left: 100px; top: 246px;
    width: 1000px; height: 707px;
    display: flex;
    box-shadow: 0 18px 40px rgba(0,0,0,.18);
  }
  .panel { position: relative; width: 500px; height: 707px; overflow: hidden; }

  /* Front cover */
  .cover { background: radial-gradient(circle at 40% 35%, var(--navy), var(--navy-deep)); }
  .cover-band { position: absolute; left: 0; bottom: 0; width: 500px; height: 120px; }
  .cover-brand {
    position: absolute; left: 44px; bottom: 110px;
    display: flex; align-items: center; gap: 12px;
  }
  .brand-square { width: 22px; height: 22px; background: var(--gold); flex: none; }
  .brand-name {
    font-weight: 500; font-size: 40px; letter-spacing: 3px; color: #ffffff;
    line-height: 1;
  }
  .brand-tagline {
    font-size: 13px; letter-spacing: 1.5px; color: var(--gold); margin-top: 6px;
    white-space: nowrap;
  }

  /* Inside sheet */
  .sheet { background: var(--paper); }
  .sheet-brand {
    position: absolute; left: 150px; top: 200px;
    display: flex; align-items: center; gap: 10px;
  }
  .sheet-brand .brand-name { color: var(--ink); font-size: 30px; letter-spacing: 2px; }
  .sheet-brand .brand-square { width: 16px; height: 16px; }
  .sheet-brand .brand-tagline { font-size: 10px; letter-spacing: 1.2px; margin-top: 4px; }

  .contact-row {
    position: absolute; left: 36px; right: 30px; bottom: 44px;
    display: flex; justify-content: space-between; align-items: center;
    font-size: 7.5px; line-height: 1.5; color: var(--muted);
  }
  .contact-item { display: flex; align-items: center; gap: 6px; white-space: nowrap; }
  .contact-icon { width: 14px; height: 14px; flex: none; }
  .sheet-rule {
    position: absolute; left: 36px; right: 30px; bottom: 22px;
    height: 6px; background: var(--navy);
  }
</style>
</head>
<body>
  <main class="folder">
    <section class="panel cover">
      <svg class="cover-band" viewBox="0 0 500 120" aria-hidden="true">
        <polygon points="0,120 500,62 500,70 0,128" fill="#f2ae1c"/>
      </svg>
      <div class="cover-brand">
        <span class="brand-square"></span>
        <div>
          <div class="brand-name">AVANTE</div>
          <div class="brand-tagline">Consultoria em Gente</div>
        </div>
      </div>
    </section>

    <section class="panel sheet">
      <div class="sheet-brand">
        <span class="brand-square"></span>
        <div>
          <div class="brand-name">AVANTE</div>
          <div class="brand-tagline">Consultoria em Gente</div>
        </div>
      </div>

      <div class="contact-row">
        <div class="contact-item">
          <svg class="contact-icon" viewBox="0 0 14 14" aria-hidden="true">
            <rect width="14" height="14" rx="2" fill="#14204a"/>
            <path d="M4 3.5l1.6-.4 1 2.1-1 .8a5 5 0 0 0 2.4 2.4l.8-1 2.1 1-.4 1.6C6.8 10.2 3.8 7.2 4 3.5z" fill="#fff"/>
          </svg>
          <span>(11) 98765-4321<br>(11) 91234-5678</span>
        </div>
        <div class="contact-item">
          <svg class="contact-icon" viewBox="0 0 14 14" aria-hidden="true">
            <rect width="14" height="14" rx="2" fill="#14204a"/>
            <path d="M7 2.5a3 3 0 0 1 3 3c0 2.2-3 5.8-3 5.8S4 7.7 4 5.5a3 3 0 0 1 3-3z" fill="#fff"/>
            <circle cx="7" cy="5.5" r="1.1" fill="#14204a"/>
          </svg>
          <span>Av. das Palmeiras, Nº 210 - Centro<br>Cidade/SP CEP 12345-000</span>
        </div>
        <div class="contact-item">
          <svg class="contact-icon" viewBox="0 0 14 14" aria-hidden="true">
            <rect width="14" height="14" rx="2" fill="#14204a"/>
            <rect x="3" y="4" width="8" height="6" fill="none" stroke="#fff" stroke-width="1"/>
            <path d="M3 4l4 3 4-3" fill="none" stroke="#fff" stroke-width="1"/>
          </svg>
          <span>contato@avanteconsult.com.br<br>www.avanteconsult.com.br</span>
        </div>
      </div>
      <div class="sheet-rule"></div>
    </section>
  </main>
</body>
</html>
```